Marketing Skill "Workouts"; Design for an e-mail attachment highlighting Marketing training subjects

I am a freelance marketing trainer based in Singapore and need to e-mail out an attachment (probably saved as a PDF) to potential clients showing the training services I offer. These clients are all large blue-chip multinational companies so the attachment needs to look professional/high quality when opened on a computer.

My Company is called "Clearpath Marketing" (logo attached)

I am assuming the size should be A4 one sided colour.

I have attached some files that show best-attempts so far. These contain the key information, but the layouts all still look rather pedestrian. I am looking for something that looks a bit more dynamic but remains clear/easy to read.

Target Market(s)

HR/Marketing managers in multinational firms, mainly consumer goods

Industry/Entity Type

Marketing

Font styles to use
Sans Serif

Colors

Designer to choose colors to be used in the design.

Requirements
Must have
• Must look modern, up-to-date, professional.
Should not have
• Not gimmicky, like a cheap deal

```html
<!DOCTYPE html>
<html lang="en">
<head>
<meta charset="utf-8">
<title>Marketing Skill Workouts – Clearpath Marketing</title>
<link href="https://fonts.googleapis.com/css2?family=Montserrat:ital,wght@0,800;1,600&family=Mulish:wght@400;600;700&display=swap" rel="stylesheet">
<style>
  :root{
    --backdrop:#3a3839;
    --brand-red:#8b1a1e;
    --brand-red-dark:#7a1519;
    --ink:#1f1f1f;
    --body-grey:#555;
    --white:#fff;
    --skin-deep:#6e4230;
    --skin-mid:#a8714f;
    --mist:#dfe3e6;
  }
  *{box-sizing:border-box;margin:0;padding:0}
  html,body{width:1200px;height:1200px;overflow:hidden;background:var(--backdrop)}
  body{font-family:"Mulish",sans-serif;position:relative}
  .flyer{position:absolute;left:50px;top:226px;width:1100px;height:777px;overflow:hidden;background:var(--mist)}
  .hero-photo{position:absolute;inset:0;
    background:
      radial-gradient(ellipse 340px 420px at 330px 360px, var(--skin-mid) 0%, var(--skin-deep) 55%, rgba(110,66,48,0) 100%),
      linear-gradient(90deg,#c9cdd1 0%,#e9ecee 60%,#d5d9dc 100%);}
  .info-panel{position:absolute;left:603px;top:0;width:450px;height:777px;
    background:linear-gradient(180deg,rgba(255,255,255,1) 0%,rgba(255,255,255,.92) 35%,rgba(245,246,247,.75) 100%)}
  .headline{position:absolute;left:107px;top:172px;font-family:"Montserrat",sans-serif;font-weight:800;font-size:56px;line-height:58px;color:var(--white)}
  .headline .accent{display:block;color:var(--brand-red)}
  .intro{position:absolute;left:107px;top:312px;width:440px;color:var(--white);font-size:23px;line-height:31px;font-weight:600}
  .intro .question{margin-bottom:12px}
  .why-me{position:absolute;left:87px;top:536px;width:471px;height:123px;background:rgba(255,255,255,.72);padding:16px 20px 0 20px;color:var(--brand-red);font-size:14.5px;line-height:18.7px}
  .why-me h3{font-family:"Montserrat",sans-serif;font-weight:800;font-size:16px;line-height:18px}
  .brand{position:absolute;right:130px;top:78px;display:flex;align-items:center;gap:14px}
  .brand-name{font-family:"Mulish",sans-serif;font-weight:400;font-size:29px;color:var(--ink)}
  .brand-dot{width:74px;height:74px;border-radius:50%;background:var(--brand-red)}
  .contact{position:absolute;right:139px;top:180px;text-align:right;color:var(--brand-red);font-weight:700;font-size:19px;line-height:28px}
  .section{position:absolute;color:var(--body-grey);font-size:14.5px;line-height:18.8px}
  .section h2{font-family:"Montserrat",sans-serif;font-weight:800;font-size:28px;line-height:30px;color:var(--brand-red);margin-bottom:2px}
  .section ul{list-style:none}
  .section li::before{content:"•";color:var(--brand-red);margin-right:5px}
  .topics{left:653px;top:302px}
  .benefits{left:626px;top:515px}
  .benefits li{color:#444}
  .tagline-band{position:absolute;left:0;top:659px;width:1100px;height:71px;background:var(--brand-red);display:flex;align-items:center;justify-content:center}
  .tagline-band p{font-family:"Montserrat",sans-serif;font-style:italic;font-weight:600;font-size:40px;color:var(--white);letter-spacing:.3px}
</style>
</head>
<body>
  <article class="flyer">
    <div class="hero-photo" role="img" aria-label="Photo of a muscular athlete's torso lifting a dumbbell in a softly lit gym"></div>
    <div class="info-panel"></div>

    <h1 class="headline">Marketing skill<span class="accent">“Workouts”</span></h1>
    <div class="intro">
      <p class="question">No time to learn?</p>
      <p>Problem solved with 1 day intensive workshops that will drive business growth and motivate your team</p>
    </div>

    <section class="why-me">
      <h3>Why me?</h3>
      <p>The latest thinking, made practical and actionable.</p>
      <p>20 years of business experience combined with over 10 years of proven training/facilitation forw major “blue-chip” clients, regularly scoring 90%+ satisfaction</p>
    </section>

    <div class="brand">
      <span class="brand-name">Clearpath Marketing</span>
      <span class="brand-dot"></span>
    </div>
    <div class="contact">
      <p>lena.marsh@clearpath-marketing.com</p>
      <p>+65 9000 4417</p>
    </div>

    <section class="section topics">
      <h2>Key Topics</h2>
      <ul>
        <li>Developing strong brand plans</li>
        <li>Writing inspiring briefs/creative evaluation</li>
        <li>Shopper marketing/developing retail promotions</li>
        <li>Brilliant launch management</li>
        <li>Improving marketing R.O.I.</li>
        <li>Driving brand growth without product innovation</li>
        <li>Insight/concept development</li>
        <li>Integrating digital channels</li>
        <li>Creatvitiy and idea generation</li>
      </ul>
    </section>

    <section class="section benefits">
      <h2>Key Benefits</h2>
      <ul>
        <li>Latest in world-class thinking/tools/case studies</li>
        <li>Ability to ‘customise’ to address your specific business issue</li>
        <li>Take-away ‘checklists’ to embed behaviours and skills</li>
        <li>Asian context/relevance</li>
        <li>Proven quality</li>
      </ul>
    </section>

    <div class="tagline-band"><p>World Class Quality without the costs</p></div>
  </article>
</body>
</html>
```